Cleaning Company needs a new business card design

Hi, We are looking for new business card designs to update with our latest logo and company information.
We would like to see designs using the colours:
Royal Blue #4169E1 - this is our company colour so this has to be in there. Please feel free to experiment with other colours.
Must include:
Front of business card:
Logo
Back of the business card:
0800 529 6081
07438 915 702
Email: info@pkrtidyhomes.co.uk
Web: www.pkrtidyhomes.co.uk
Services:
End of Tenancy
Carpet & Upholstery
Regular & One Off
all work fully insured.
The front of the business card with the logo can be made to look raised print. The blue man to be a shiny finish.
The business card needs to be presented in a matt finish
The business must be in the following styles:
Standard Square with rounded corners.
Thank you to all that take part in this.
Target Market(s)
Men and Women of different ages in the UK.
Industry/Entity Type
House Cleaning
Contact Information for Business Card
Front of business card:
Logo
0800 529 6081
07438 915 702
Email: pkrtidy@mailbox-demo.co.uk
Services:
End of Tenancy
Carpet & Upholstery
Regular & One Off
all work fully insured.

```html
<!DOCTYPE html>
<html lang="en">
<head>
<meta charset="utf-8">
<title>PKR Tidy Homes – Business Cards</title>
<link rel="stylesheet" href="https://fonts.googleapis.com/css2?family=Questrial&family=Montserrat:wght@700&display=swap">
<style>
  :root {
    --brand-blue: #1b2fe6;
    --deep-blue: #0b2bb8;
    --sky-blue: #4aa8f0;
    --ink: #111418;
    --paper: #ffffff;
    --backdrop: #e4e8ee;
  }
  * { margin: 0; padding: 0; box-sizing: border-box; }
  html, body { width: 1200px; height: 833px; overflow: hidden; }
  body { background: var(--backdrop); position: relative; }

  .card { position: absolute; top: 262px; width: 467px; height: 300px; overflow: hidden; }
  .card--info { left: 87px; background: var(--paper); }
  .card--logo { left: 645px; }

  /* info side */
  .info-divider { position: absolute; left: 423px; top: 0; width: 6px; height: 300px; background: var(--brand-blue); }
  .insured-band { position: absolute; left: 0; top: 257px; width: 429px; height: 43px; background: var(--brand-blue); }
  .info-panel { position: absolute; left: 0; top: 0; width: 423px; height: 257px; background: var(--paper); border-bottom-right-radius: 20px; }
  .stripe { position: absolute; top: 0; height: 300px; background: var(--brand-blue); }
  .stripe--one { left: 434px; width: 5px; }
  .stripe--two { left: 443px; width: 6px; }
  .stripe--three { left: 453px; width: 14px; }

  .brand-name { position: absolute; font-family: "Montserrat", sans-serif; font-weight: 700; color: var(--brand-blue); line-height: 1; }
  .card--info .brand-name { left: 26px; top: 34px; }
  .brand-name .brand-main { display: block; font-size: 58px; letter-spacing: -1px; }
  .brand-name .brand-sub { display: block; font-size: 15px; margin-top: 6px; }

  .services { position: absolute; left: 221px; top: 70px; list-style: none; font-family: "Questrial", sans-serif; font-size: 17.5px; line-height: 21.5px; color: var(--ink); }
  .freephone { position: absolute; left: 153px; top: 160px; font-family: "Questrial", sans-serif; font-size: 22px; letter-spacing: 0.5px; color: var(--ink); }
  .contacts { position: absolute; left: 25px; top: 192px; list-style: none; font-family: "Questrial", sans-serif; font-size: 16px; line-height: 21px; color: var(--ink); }
  .insured { position: absolute; left: 25px; top: 270px; font-family: "Montserrat", sans-serif; font-weight: 700; font-size: 15.5px; color: var(--paper); }

  /* logo side */
  .glow-backdrop { position: absolute; inset: 0;
    background:
      radial-gradient(ellipse 190px 140px at 255px 150px, #ffffff 0%, #e8f6ff 35%, #9fd8fb 60%, rgba(60,140,240,0) 100%),
      radial-gradient(ellipse 330px 240px at 250px 140px, #3d8af2 0%, #1f5fe0 55%, #0a2fa8 100%); }
  .card--logo .brand-name { left: 0; width: 467px; top: 96px; text-align: center; }
  .card--logo .brand-main { font-size: 76px; }
  .card--logo .brand-sub { font-size: 18px; margin-top: 8px; }
</style>
</head>
<body>
  <section class="card card--info" aria-label="Business card contact side">
    <div class="info-divider"></div>
    <div class="insured-band"></div>
    <div class="info-panel"></div>
    <div class="stripe stripe--one"></div>
    <div class="stripe stripe--two"></div>
    <div class="stripe stripe--three"></div>

    <div class="brand-name"><span class="brand-main">PKR</span><span class="brand-sub">Tidy Homes Limited</span></div>

    <ul class="services">
      <li>End of Tenancy</li>
      <li>Carpet &amp; Upholstery</li>
      <li>Regular &amp; One Off</li>
    </ul>

    <p class="freephone">0800 529 6081</p>

    <ul class="contacts">
      <li>07438 915 702</li>
      <li>pkrtidy@mailbox-demo.co.uk</li>
      <li>www.pkrtidyhomes.co.uk</li>
    </ul>

    <p class="insured">ALL WORK FULLY INSURED</p>
  </section>

  <section class="card card--logo" aria-label="Business card logo side">
    <div class="glow-backdrop" role="img" aria-label="Swirling blue light background with a bright white glow in the centre"></div>
    <div class="brand-name"><span class="brand-main">PKR</span><span class="brand-sub">Tidy Homes Limited</span></div>
  </section>
</body>
</html>
```